依頼詳細
デザインテイストのイメージは以下の通りです
・洗練された
・安心感のある
・落ち着いた
・信頼できる

「写真素材について」
事業所画像など一部提供可能ですが、基本的にはミルテフォトなどの素材もしくはイラストとの組み合わせでお願いいたします

「WFと原稿について」
レイアウトについてはある程度自由に変更していただいても結構です

「納品形態について」
psd xd aiなど劣化のないものであればなんでも大丈夫です

「選考のポイント」
デザイン性のみ
SEOやマーケティング的な提案は求めていません
元サイトURL一応載せておきますが形式的に作成したものですので
こちらと比較してのアドバイスなども求めていません
あくまでデザインで決めます

サイトURL
http://kurete-kaigo.net/
ページ数
5ページ
希望イメージ
シンプル 複雑
単色 カラフル
暗い 明るい
日常 高級
遊び心 厳粛
未来的 伝統的
女性的 男性的
希望する色
青系、水色系
納品ファイル
• 高解像度JPG (.jpg)
• イラストレーター形式 (.ai)
• フォトショップ形式 (.psd)
• PNG形式 (.png)
補足説明
提案の数が少ないので期限を延長いたします
■ 選んだ理由

限定された条件のなかで素晴らしいデザインをご提案いただきありがとうございました

■ 提案者全員のお礼・コメント

素材画像がない状態でのデザイン制作は難しかったと思います
その中で素晴らしい提案をいただきまして本当にありがとうございました

```html
<!DOCTYPE html>
<html lang="ja">
<head>
<meta charset="utf-8">
<title>ホームケア くれて</title>
<link href="https://fonts.googleapis.com/css2?family=Noto+Sans+JP:wght@400;500;700&family=Noto+Serif+JP:wght@500;700&family=Montserrat:wght@500;700&display=swap" rel="stylesheet">
<style>
:root{
  --blue:#1f7fc4;
  --blue-dark:#16629a;
  --sky:#eaf4fb;
  --sky-2:#d6e9f6;
  --navy:#1c3550;
  --text:#333a42;
  --muted:#6b7580;
  --line:#dfe6ec;
  --white:#ffffff;
}
*{margin:0;padding:0;box-sizing:border-box}
html,body{width:1200px;height:2796px;overflow:hidden}
body{font-family:"Noto Sans JP",sans-serif;color:var(--text);background:var(--white);position:relative;font-size:15px;line-height:1.8}
.site-header{position:absolute;top:0;left:0;width:1200px;height:78px;display:flex;align-items:center;justify-content:space-between;padding:0 44px;background:var(--white)}
.brand{display:flex;align-items:center;gap:10px;font-weight:700;font-size:24px;color:var(--blue)}
.brand-dot{width:18px;height:18px;border-radius:50%;background:var(--blue)}
.brand small{font-size:12px;font-weight:500;display:block;line-height:1;margin-bottom:2px}
.global-nav{display:flex;gap:34px;font-size:14px;font-weight:500;color:var(--text)}
.hero{position:absolute;top:78px;left:0;width:1200px;height:490px;background:linear-gradient(100deg,#d7dde3 0%,#f1f3f5 45%,#e4e8ec 100%)}
.hero-label{position:absolute;left:0;right:0;top:225px;text-align:center;font-family:"Montserrat",sans-serif;font-weight:700;font-size:40px;letter-spacing:4px;color:rgba(255,255,255,.75)}
.intro{position:absolute;top:596px;left:0;width:1200px;text-align:center}
.badge{display:inline-block;background:var(--blue);color:var(--white);font-size:14px;font-weight:500;padding:4px 22px;border-radius:20px}
.intro h1{font-size:27px;font-weight:700;margin-top:22px;letter-spacing:1px;color:var(--navy)}
.intro p{margin-top:18px;font-size:14px;color:var(--muted);line-height:1.9}
.feature-cards{position:absolute;top:880px;left:50px;width:1100px;display:flex;gap:40px}
.feature-card{width:530px;height:350px;border:1px solid var(--line);background:var(--white)}
.feature-photo{height:200px;background:linear-gradient(120deg,#9aa6b2,#cfd6dd)}
.feature-photo.alt{background:linear-gradient(120deg,#5e7080,#b8c2cb)}
.feature-card h3{font-size:17px;font-weight:700;margin:18px 24px 6px;color:var(--navy)}
.feature-card p{font-size:12.5px;color:var(--muted);margin:0 24px;line-height:1.8}
.pill-btn{display:inline-flex;align-items:center;gap:8px;background:var(--blue-dark);color:var(--white);font-size:14px;font-weight:500;border-radius:24px}
.features-more{position:absolute;top:1284px;left:480px;width:240px;height:38px;justify-content:center}
.services{position:absolute;top:1400px;left:0;width:1200px;height:400px}
.services svg.wave{position:absolute;top:0;left:0}
.section-title{font-family:"Noto Serif JP",serif;font-weight:700;font-size:26px;color:var(--blue-dark);text-align:center}
.services .section-title{position:absolute;top:112px;width:100%}
.service-cards{position:absolute;top:160px;left:50px;width:1100px;display:flex;gap:40px}
.service-card{width:530px;height:190px;background:var(--white);border:1px solid var(--line);display:flex;padding:22px;gap:22px;position:relative}
.service-avatar{width:120px;height:120px;border-radius:50%;flex:none;background:linear-gradient(160deg,#d9e7f2,#b9cfe0)}
.service-card h3{font-size:17px;color:var(--blue-dark);font-weight:700}
.service-card p{font-size:12.5px;color:var(--muted);line-height:1.8;margin-top:6px}
.learn-btn{position:absolute;right:18px;bottom:14px;background:var(--blue-dark);color:var(--white);font-family:"Montserrat",sans-serif;font-size:11px;padding:3px 14px;border-radius:3px}
.info-grid{position:absolute;top:1830px;left:50px;width:1100px;display:grid;grid-template-columns:530px 530px;column-gap:40px;row-gap:44px}
.info-box{border:1px solid var(--line);background:var(--white);padding:22px 26px;position:relative}
.info-box::before{content:"";position:absolute;left:0;top:0;border-top:18px solid var(--blue);border-right:18px solid transparent}
.info-box h2{font-size:18px;font-weight:700;color:var(--navy);border-bottom:1px solid var(--line);padding-bottom:10px;margin-bottom:10px}
.news-list{list-style:none;font-size:12.5px}
.news-list li{display:flex;gap:24px;padding:9px 0;border-bottom:1px dashed var(--line)}
.news-list time{color:var(--muted);width:80px}
.recruit p{font-size:12.5px;line-height:1.85;margin-bottom:10px}
.recruit strong{color:var(--blue-dark)}
.tall{height:400px}
.short{height:190px}
.usage p{font-size:12.5px;color:var(--muted);line-height:1.9}
.contact-row{display:flex;align-items:center;gap:12px;margin-top:8px}
.contact-row .tel{font-family:"Montserrat",sans-serif;font-weight:700;font-size:22px;color:var(--navy)}
.contact-row small{font-size:11px;color:var(--muted)}
.contact-row .mail{font-family:"Montserrat",sans-serif;font-weight:500;font-size:18px;color:var(--navy)}
.icon-box{width:30px;height:30px;border-radius:4px;background:var(--blue);display:flex;align-items:center;justify-content:center}
.bottom-wave{position:absolute;top:2520px;left:0}
.site-footer{position:absolute;top:2752px;left:0;width:1200px;height:44px;background:var(--navy);color:var(--white);font-size:11px;text-align:center;line-height:44px;font-family:"Montserrat",sans-serif}
</style>
</head>
<body>
<header class="site-header">
  <div class="brand"><span class="brand-dot"></span><div><small>ホームケア</small>くれて</div></div>
  <nav class="global-nav"><span>特長</span><span>ご利用について</span><span>提供サービス</span><span>事業所一覧</span><span>採用情報</span><span>お問い合わせ</span></nav>
</header>

<section class="hero" role="img" aria-label="タブレットを持つ介護スタッフの女性の写真">
  <div class="hero-label">HOMECARE SERVICE</div>
</section>

<section class="intro">
  <span class="badge">24時間365日対応</span>
  <h1>住み慣れたご自宅で自分らしい介護サービスを</h1>
  <p>自宅での生活を続けたい方へ、訪問介護・居宅介護支援のサービスを提供しています。<br>1日24時間、年中無休でご利用者様とご家族の暮らしを支えるサービスを心がけております。<br>スタッフ一同ともに歩み、地域に寄り添うケアを大切にしています。</p>
</section>

<div class="feature-cards">
  <article class="feature-card">
    <div class="feature-photo" role="img" aria-label="書類を前に相談するスタッフの写真"></div>
    <h3>1人ひとりに最適な個別支援</h3>
    <p>経験豊富なケアマネジャーがご本人とご家族の想いを伺い、生活状況に合わせたケアプランを作成します。必要に応じて計画を見直し、安心の暮らしを支えます。</p>
  </article>
  <article class="feature-card">
    <div class="feature-photo alt" role="img" aria-label="車いすの高齢者に寄り添うスタッフの写真"></div>
    <h3>高齢者から障がい児・児童まで</h3>
    <p>高齢の方はもちろん、障がいのある方やお子さまにも対応しています。経験を積んだスタッフが、一人ひとりに合わせた丁寧なサービスをお届けします。</p>
  </article>
</div>

<a class="pill-btn features-more">
  <svg width="14" height="14" viewBox="0 0 14 14"><circle cx="7" cy="7" r="7" fill="#fff"/><path d="M5.5 4l3 3-3 3" stroke="#16629a" stroke-width="1.6" fill="none"/></svg>
  くれての介護サービス特徴
</a>

<section class="services">
  <svg class="wave" width="1200" height="400" viewBox="0 0 1200 400"><path d="M0 60 C300 0 600 120 900 50 S1150 20 1200 40 L1200 400 L0 400Z" fill="#eaf4fb"/></svg>
  <h2 class="section-title">提供サービスのご紹介</h2>
  <div class="service-cards">
    <article class="service-card">
      <div class="service-avatar" role="img" aria-label="訪問介護スタッフのイラスト"></div>
      <div><h3>訪問介護</h3><p>専門資格を持つヘルパーがご自宅を訪問し、食事や入浴などの身体介護、掃除や買い物などの生活援助を行います。</p></div>
      <span class="learn-btn">Learn More</span>
    </article>
    <article class="service-card">
      <div class="service-avatar" role="img" aria-label="居宅介護支援スタッフのイラスト"></div>
      <div><h3>居宅介護支援</h3><p>ケアマネジャーがご相談を伺い、介護保険の申請代行やケアプランの作成など、適切なサービスを調整いたします。</p></div>
      <span class="learn-btn">Learn More</span>
    </article>
  </div>
</section>

<div class="info-grid">
  <section class="info-box tall">
    <h2>ニュース</h2>
    <ul class="news-list">
      <li><time>2021.05.10</time><span>ウェブサイトをリニューアルしました</span></li>
      <li><time>2021.04.22</time><span>新事業所がオープンしました</span></li>
      <li><time>2021.04.01</time><span>サービス提供時間の案内を更新しました</span></li>
      <li><time>2021.03.15</time><span>訪問ヘルパー募集の案内を掲載しました</span></li>
      <li><time>2021.02.20</time><span>ウェブサイトをリニューアルしました</span></li>
      <li><time>2021.01.08</time><span>新事業所がオープンしました</span></li>
    </ul>
  </section>
  <section class="info-box tall recruit">
    <h2>スタッフ随時募集中</h2>
    <p>「介護の仕事に興味がある」「経験を活かしたい」方のご応募をお待ちしております。</p>
    <p><strong>事務職・ホテル・介護職</strong><br>ヘルパー、事務、管理者などさまざまな職種を募集中です。</p>
    <p><strong>週1日〜勤務・資格手当あり</strong><br>曜日・時間の相談可。研修制度も整っています。</p>
    <p><strong>資格・経験不問</strong><br>未経験の方も安心してスタートできるサポート体制です。</p>
  </section>
  <section class="info-box short usage">
    <h2>ご利用について</h2>
    <p>ご利用の流れやご相談方法についてご案内します。まずはお気軽にお問い合わせください。担当ケアマネジャーがご自宅に伺いご説明いたします。</p>
  </section>
  <section class="info-box short">
    <h2>無料相談受付中</h2>
    <div class="contact-row">
      <span class="icon-box"><svg width="16" height="16" viewBox="0 0 16 16"><path d="M3 1.5l3 3-1.5 2a9 9 0 0 0 5 5l2-1.5 3 3-2 2C6 14 2 10 1.5 3.5z" fill="#fff"/></svg></span>
      <span class="tel">098-555-0127</span><small>受付 9:00〜18:00</small>
    </div>
    <div class="contact-row">
      <span class="icon-box"><svg width="16" height="12" viewBox="0 0 16 12"><rect x="0.5" y="0.5" width="15" height="11" fill="none" stroke="#fff"/><path d="M1 1l7 6 7-6" stroke="#fff" fill="none"/></svg></span>
      <span class="mail">info@kurete-kaigo.net</span>
    </div>
  </section>
</div>

<svg class="bottom-wave" width="1200" height="232" viewBox="0 0 1200 232"><path d="M0 120 C250 60 500 170 800 110 S1100 70 1200 100 L1200 232 L0 232Z" fill="#eaf4fb"/><path d="M0 170 C300 120 600 210 900 160 S1150 140 1200 150 L1200 232 L0 232Z" fill="#d6e9f6"/></svg>

<footer class="site-footer">Kurete All rights reserved.</footer>
</body>
</html>
```